Веб-сайт для застройщика под греческую золотую визу Veltaroon.gr
застройщик под греческую золотую визу Veltaroon.gr
Veltaroon.gr
https://morvilo-estates.com/
https://tpk.example/
Veltaroon Development IKE — Website Design Brief
Домен: veltaroon.gr
Название Veltaroon является авторским сочетанием слов:
Hellenic
Premium
Название должно ассоциироваться с:
premium Mediterranean lifestyle
boutique investment real estate
комфортом и эстетикой
Это можно опционально и ненавязчиво обыгрывать в дизайне:
через typography
через premium визуальные акценты
через Mediterranean aesthetic
через сочетание natural + premium visual language
Важно:
Бренд не должен выглядеть overly luxury или “gold-plated wealth style”.
Основной акцент:
tasteful premium
calm confidence
boutique sophistication
1. О компании
Veltaroon Development IKE — девелоперская компания в Греции, которая занимается:
покупкой и реновацией зданий
созданием boutique apartments
продажей недвижимости под Greek Golden Visa
дальнейшим управлением арендой для инвесторов
2. Основная идея сайта
Главный акцент:
Greek Golden Visa
инвестиции в недвижимость в Греции
получение ВНЖ в Европе
комфортный Mediterranean lifestyle
Важно показать, что компания делает проекты «с душой»:
натуральные материалы
светлое дерево
мягкий olive green
уютные современные интерьеры
boutique Mediterranean aesthetics
3. Сайт должен выглядеть
premium
trustworthy
modern
investment-oriented
4. Сайт НЕ должен выглядеть
как агентство недвижимости
как дешёвый Golden Visa landing page
как обычная строительная компания
5. Целевая аудитория
Средний возраст клиентов: 45+ лет, семейные инвесторы, часто ищущие решение для всей семьи.
Инвесторы и семьи из:
Китай
Турция
СНГ
Middle East
Основная цель клиентов:
получение ВНЖ в Европе через Greek Golden Visa
покупка доходной недвижимости
инвестиции в недвижимость в ЕС
6. Основное меню
Greek Golden Visa или просто Golden Visa
Projects
Investors
Partners
Contact (внутри Contact раздела будет вставка About Us либо же вставка будет сразу на главной странице - на ваше усмотрение)
Дополнительно:
Client Login (отдельный кабинет для покупателей квартир / инвесторов)
7. Языки сайта
EN (по умолчанию)
GR
RU
中文
TR
8. Визуальная стилистика
Эстетика
Mediterranean vibe
boutique living vibe
premium natural materials
Цвета:
olive green
warm white
beige
soft stone grey
(Цвета даны справочно и могут адаптироваться дизайнером)
UI стиль:
clean
calm
ВАЖНО:
Полное техническое задание не влезло в описание и размещено в открытом виде на внешнем файлообменнике в текстовом файле:
https://filebarrow.example/k4Rq8
или
https://sklad-faylov.example/7pLmz

```html
<!DOCTYPE html>
<html lang="en">
<head>
<meta charset="utf-8">
<title>Veltaroon Development — Premium Greek Living & Golden Visa Investments</title>
<link href="https://fonts.googleapis.com/css2?family=Cormorant+Garamond:wght@400;500;600&family=Inter:wght@400;500;600&display=swap" rel="stylesheet">
<style>
:root{
  --green:#27321f;
  --olive:#857546;
  --gold:#a3915e;
  --gold-light:#c2b27f;
  --bg:#f4f1ec;
  --card:#ece7df;
  --ink:#1e211b;
  --muted:#5d5b55;
  --line:#dcd6cc;
  --white:#fbf9f5;
  --on-dark:#e4e2dc;
  --on-dark-head:#cfc9bb;
}
*{box-sizing:border-box;margin:0;padding:0}
html,body{width:1200px;height:2384px;overflow:hidden}
body{background:var(--bg);font-family:"Inter",sans-serif;color:var(--ink);position:relative}
.abs{position:absolute}
.eyebrow{font-size:11.5px;letter-spacing:1.6px;color:var(--olive);font-weight:500;text-transform:uppercase}
.h2{font-family:"Cormorant Garamond",serif;font-weight:500;font-size:32px;line-height:34px;color:var(--ink)}
.icon{stroke:var(--gold);fill:none;stroke-width:1.4;stroke-linecap:round;stroke-linejoin:round}

/* header */
.site-header{left:0;top:0;width:1200px;height:80px;background:var(--green);display:flex;align-items:center;padding:0 40px}
.brand{display:flex;align-items:center;gap:12px;color:var(--white);font-family:"Cormorant Garamond",serif;font-weight:600;font-size:19px;letter-spacing:3.5px}
.brand-mark{width:22px;height:22px;border:1.5px solid var(--gold)}
.main-nav{margin-left:auto;display:flex;gap:45px;align-items:center;font-size:12.5px;letter-spacing:.4px;color:var(--white)}
.lang{display:flex;align-items:center;gap:5px;font-size:11px}

/* hero */
.hero-media{left:472px;top:80px;width:728px;height:489px;background:linear-gradient(100deg,var(--bg) 0%,rgba(244,241,236,0) 14%),linear-gradient(180deg,#e9c8a0 0%,#c9a27a 28%,#8fa0a8 55%,#6f8ea0 70%,#d8cfc2 82%,#cbbfae 100%)}
.hero-copy{left:82px;top:150px;width:480px}
.hero-title{font-family:"Cormorant Garamond",serif;font-weight:500;font-size:49px;line-height:56px;color:var(--ink)}
.hero-title span{color:var(--olive)}
.hero-rule{width:60px;height:1px;background:var(--olive);margin:26px 0 24px}
.hero-lead{font-family:"Cormorant Garamond",serif;font-size:19px;line-height:26px;color:#333}
.btn-row{display:flex;gap:14px;margin-top:30px}
.btn{height:43px;display:flex;align-items:center;justify-content:center;font-size:11.5px;letter-spacing:.8px}
.btn-dark{background:var(--green);color:var(--white);width:174px}
.btn-line{border:1px solid #bdb6aa;color:var(--ink);width:138px;background:var(--white)}

/* features */
.features{left:40px;top:569px;width:1160px;height:152px;border-top:1px solid var(--line);display:flex;justify-content:center;padding-top:24px}
.feature{width:256px;display:flex;flex-direction:column;align-items:center;text-align:center;font-size:12.5px;line-height:18px;color:#333;border-right:1px solid var(--line);height:105px}
.feature:last-child{border-right:none}
.feature svg{margin-bottom:12px}

/* about */
.about-panel{left:20px;top:735px;width:375px;height:416px;background:var(--green);padding:48px 62px 0 62px;color:var(--white)}
.about-panel .eyebrow{color:var(--gold-light)}
.about-title{font-family:"Cormorant Garamond",serif;font-weight:500;font-size:36px;line-height:44px;margin:18px 0 22px}
.about-text{font-size:11.8px;line-height:20px;color:var(--on-dark)}
.link-line{display:inline-flex;gap:14px;align-items:center;margin-top:26px;font-size:11px;letter-spacing:.6px;border-bottom:1px solid currentColor;padding-bottom:4px}
.about-media{left:395px;top:735px;width:496px;height:416px;background:linear-gradient(180deg,#e6d6bd 0%,#d6bf9c 45%,#bfa27c 75%,#a6896a 100%)}
.values{left:910px;top:745px;width:270px;height:406px;background:var(--card);padding:38px 30px;display:flex;flex-direction:column;gap:46px}
.value{display:flex;align-items:center;gap:20px;font-size:12.8px;line-height:18px;color:#333}

/* projects */
.projects-head{left:82px;top:1174px}
.projects-head .h2{margin-top:14px}
.slider-ctrl{left:1018px;top:1194px;display:flex;gap:12px}
.circle-btn{width:30px;height:30px;border:1px solid #6a6a60;border-radius:50%;display:flex;align-items:center;justify-content:center}
.project-card{top:1275px;height:289px;background:var(--white);border:1px solid var(--line)}
.project-media{height:163px}
.project-body{padding:14px 20px}
.project-name{font-family:"Cormorant Garamond",serif;font-size:20px;font-weight:500}
.project-desc{font-size:11px;line-height:15px;color:var(--muted);margin-top:10px;width:230px}
.project-link{display:flex;justify-content:space-between;width:247px;font-size:10px;letter-spacing:.4px;margin-top:14px;border-bottom:1px solid #999;padding-bottom:5px}
.abs.view-all{background:var(--green);color:var(--white);display:flex;flex-direction:column;align-items:center;justify-content:center;text-align:center;font-size:14px;letter-spacing:1.4px;line-height:20px;gap:14px;border:none}

/* investors */
.investors{left:40px;top:1590px;width:1120px;border-top:1px solid var(--line)}
.inv-copy{left:82px;top:1614px;width:300px}
.inv-copy .h2{margin:12px 0 16px}
.inv-text{font-size:12px;line-height:18px;color:#333;width:200px}
.inv-btn{margin-top:20px;width:133px;height:34px;font-size:10.5px}
.inv-grid{left:394px;top:1624px;width:720px;display:grid;grid-template-columns:repeat(3,1fr);gap:18px 12px}
.inv-item{height:86px;border:1px solid var(--line);background:var(--white);display:flex;align-items:center;gap:16px;padding:0 18px}
.inv-item h4{font-size:11.5px;font-weight:600;margin-bottom:4px}
.inv-item p{font-size:10.3px;line-height:16px;color:var(--muted)}

/* news */
.news-line{left:40px;top:1856px;width:1120px;border-top:1px solid var(--line)}
.news-copy{left:82px;top:1876px}
.news-copy .h2{font-size:34px;line-height:38px;margin-top:14px}
.news-card{top:1888px;width:187px;height:215px;background:var(--card)}
.news-media{height:96px}
.news-body{padding:16px 13px}
.news-date{font-size:8px;color:#8b877f;letter-spacing:.4px}
.news-title{font-family:"Cormorant Garamond",serif;font-size:14.5px;line-height:17px;margin-top:8px;height:36px}
.news-more{font-size:9.5px;color:var(--olive);margin-top:14px;display:flex;align-items:center;gap:8px;font-weight:500}

/* footer */
.site-footer{left:0;top:2133px;width:1200px;height:251px;background:var(--green)}
.on-dark{color:var(--on-dark)}
.f-brand{left:80px;top:2168px}
.f-brand .brand{font-size:17px}
.f-about{left:80px;top:2210px;width:180px;font-size:10.5px;line-height:17px}
.socials{left:80px;top:2285px;display:flex;gap:14px}
.socials span{width:30px;height:30px;border:1px solid var(--gold);border-radius:50%}
.f-col{top:2168px;font-size:11px;line-height:21px}
.f-col h5,.newsletter h5{font-size:10.5px;letter-spacing:1px;font-weight:500;margin-bottom:10px;color:var(--on-dark-head)}
.f-contact{display:flex;align-items:center;gap:8px}
.newsletter{left:891px;top:2165px;width:228px;height:154px;border:1px solid #7c8070;padding:22px 18px}
.newsletter h5{margin-bottom:0}
.newsletter p{font-size:10.5px;line-height:17px;margin-top:14px}
.nl-form{display:flex;margin-top:16px;height:36px}
.nl-input{flex:1;background:var(--white);color:#6d6a63;font-size:11px;display:flex;align-items:center;padding-left:12px}
.nl-submit{width:38px;background:#c4ad6e;display:flex;align-items:center;justify-content:center}
.f-bottom{left:80px;top:2345px;width:1040px;border-top:1px solid #47523d;display:flex;justify-content:space-between;padding-top:14px;font-size:9px}
</style>
</head>
<body>

<header class="site-header abs">
  <div class="brand"><span class="brand-mark"></span>VELTAROON</div>
  <nav class="main-nav">
    <span>GOLDEN VISA</span><span>PROJECTS</span><span>INVESTORS</span><span>PARTNERS</span><span>ABOUT US</span><span>CONTACT</span>
    <span class="lang"><svg width="12" height="12" viewBox="0 0 12 12"><circle cx="6" cy="6" r="5" fill="none" stroke="#fbf9f5"/><path d="M1 6h10M6 1c-2 3-2 7 0 10M6 1c2 3 2 7 0 10" fill="none" stroke="#fbf9f5" stroke-width=".8"/></svg>EN ⌄</span>
  </nav>
</header>

<div class="hero-media abs" role="img" aria-label="Modern villa terrace with infinity pool, olive tree and lounge sofas overlooking the sea at sunset"></div>
<section class="hero-copy abs">
  <h1 class="hero-title"><span>Premium Greek</span><br>Living &amp; Golden Visa<br>Investments</h1>
  <div class="hero-rule"></div>
  <p class="hero-lead">Boutique residences thoughtfully designed<br>for modern living and long-term investment.</p>
  <div class="btn-row"><span class="btn btn-dark">EXPLORE PROJECTS</span><span class="btn btn-line">GOLDEN VISA</span></div>
</section>

<section class="features abs">
  <div class="feature"><svg class="icon" width="34" height="34" viewBox="0 0 34 34"><path d="M5 12L17 5l12 7zM7 14h20M9 15v12M14 15v12M20 15v12M25 15v12M5 29h24"/></svg>Real estate<br>investments<br>in Greece</div>
  <div class="feature"><svg class="icon" width="36" height="36" viewBox="0 0 36 36"><circle cx="18" cy="18" r="16"/><path d="M18 27V15M18 20c-5 0-7-3-7-7 4 0 7 2 7 7zM18 20c5 0 7-3 7-7-4 0-7 2-7 7z"/></svg>Obtaining a residence<br>permit in Europe</div>
  <div class="feature"><svg class="icon" width="38" height="34" viewBox="0 0 38 34"><path d="M11 18a8 8 0 0 1 16 0M19 4v4M9 9l3 3M29 9l-3 3M4 18h30M4 23c4-3 6 3 10 0s6 3 10 0 6 3 10 0M4 28c4-3 6 3 10 0s6 3 10 0 6 3 10 0"/></svg>Comfortable<br>Mediterranean<br>lifestyle</div>
  <div class="feature"><svg class="icon" width="34" height="36" viewBox="0 0 34 36"><path d="M17 3l12 5v9c0 8-5 13-12 16C10 30 5 25 5 17V8z"/><path d="M17 26V14M17 20c-3 0-5-2-5-5 3 0 5 2 5 5zM17 18c3 0 5-2 5-5-3 0-5 2-5 5z"/></svg>Secure &amp; transparent<br>investment<br>process</div>
</section>

<section class="about-panel abs">
  <p class="eyebrow">About us</p>
  <h2 class="about-title">More than<br>buildings.<br>It’s about legacy.</h2>
  <p class="about-text">Veltaroon Development IKE is a Greek development company creating boutique residences that combine timeless architecture, prime locations and the benefits of the Greek Golden Visa.</p>
  <span class="link-line">OUR STORY <svg width="12" height="8" viewBox="0 0 12 8"><path d="M1 4h10M8 1l3 3-3 3" fill="none" stroke="#fbf9f5"/></svg></span>
</section>
<div class="about-media abs" role="img" aria-label="Bright living room with arched windows, cream sofas and wooden furniture overlooking the sea"></div>
<aside class="values abs">
  <div class="value"><svg class="icon" width="34" height="30" viewBox="0 0 34 30"><path d="M3 10l6-7h16l6 7-14 17zM3 10h28M12 3l-3 7 8 17 8-17-3-7"/></svg>Timeless<br>architecture</div>
  <div class="value"><svg class="icon" width="34" height="32" viewBox="0 0 34 32"><path d="M17 29s-9-10-9-16a9 9 0 0 1 18 0c0 6-9 16-9 16z"/><circle cx="17" cy="13" r="3.5"/></svg>Prime<br>locations</div>
  <div class="value"><svg class="icon" width="34" height="32" viewBox="0 0 34 32"><path d="M17 2l11 4v8c0 8-5 13-11 16C11 27 6 22 6 14V6z"/><path d="M12 16l4 4 7-8"/></svg>Built for<br>tomorrow</div>
  <div class="value"><svg class="icon" width="36" height="30" viewBox="0 0 36 30"><circle cx="18" cy="9" r="5"/><circle cx="7" cy="12" r="3.5"/><circle cx="29" cy="12" r="3.5"/><path d="M9 27c0-6 4-10 9-10s9 4 9 10M1 26c0-5 3-8 6-8M35 26c0-5-3-8-6-8"/></svg>Personalized<br>service</div>
</aside>

<div class="projects-head abs">
  <p class="eyebrow">Our projects</p>
  <h2 class="h2">Curated residences<br>in prime locations</h2>
</div>
<div class="slider-ctrl abs">
  <span class="circle-btn"><svg width="8" height="10" viewBox="0 0 8 10"><path d="M6 1L2 5l4 4" fill="none" stroke="#333"/></svg></span>
  <span class="circle-btn"><svg width="8" height="10" viewBox="0 0 8 10"><path d="M2 1l4 4-4 4" fill="none" stroke="#333"/></svg></span>
</div>
<article class="project-card abs" style="left:82px;width:471px">
  <div class="project-media" role="img" aria-label="Contemporary white villa with pool and panoramic sea views" style="background:linear-gradient(180deg,#b9c2c6 0%,#d7c6aa 50%,#8f8a78 100%)"></div>
  <div class="project-body">
    <h3 class="project-name">Residence in Athens</h3>
    <p class="project-desc">Contemporary villa with panoramic city &amp; sea views</p>
    <div class="project-link"><span>VIEW PROJECT</span><span>→</span></div>
  </div>
</article>
<article class="project-card abs" style="left:578px;width:366px">
  <div class="project-media" role="img" aria-label="Elegant apartment interior with tall windows facing the Athens skyline" style="background:linear-gradient(180deg,#c9cdca 0%,#b8ad97 55%,#7b6c55 100%)"></div>
  <div class="project-body">
    <h3 class="project-name">Athens Hall</h3>
    <p class="project-desc">Elegant apartments in the heart<br>of Athens</p>
    <div class="project-link"><span>VIEW PROJECT</span><span>→</span></div>
  </div>
</article>
<div class="project-card view-all abs" style="left:966px;width:148px">
  <svg class="icon" width="34" height="32" viewBox="0 0 34 32"><path d="M5 11L17 4l12 7zM6 11v18h22V11M11 15v11M17 15v11M23 15v11M4 29h26"/></svg>
  <span>VIEW ALL<br>PROJECTS</span>
</div>

<div class="investors abs"></div>
<section class="inv-copy abs">
  <p class="eyebrow">For investors</p>
  <h2 class="h2">New opportunities.<br>Long-term growth.</h2>
  <p class="inv-text">We create valuable real estate in Greece with clear benefits for international investors.</p>
  <span class="btn btn-dark inv-btn">INVEST WITH US</span>
</section>
<div class="inv-grid abs">
  <div class="inv-item"><svg class="icon" width="38" height="38" viewBox="0 0 38 38"><path d="M17 5a15 15 0 1 0 15 15H17z"/><path d="M21 2v14h14A14 14 0 0 0 21 2z"/></svg><div><h4>Diverse portfolio</h4><p>Residential &amp; commercial properties in prime locations</p></div></div>
  <div class="inv-item"><svg class="icon" width="38" height="38" viewBox="0 0 38 38"><path d="M4 34h30M7 34V24h4v10M15 34V18h4v16M23 34V12h4v22M31 34V6"/><path d="M6 16l9-6 8 4 9-9"/></svg><div><h4>Market stability</h4><p>Greece is among the most stable EU real estate markets</p></div></div>
  <div class="inv-item"><svg class="icon" width="40" height="34" viewBox="0 0 40 34"><circle cx="20" cy="10" r="5"/><circle cx="8" cy="13" r="4"/><circle cx="32" cy="13" r="4"/><path d="M11 30c0-6 4-10 9-10s9 4 9 10zM1 28c0-5 3-8 7-8M39 28c0-5-3-8-7-8"/></svg><div><h4>Growing demand</h4><p>Tourism &amp; relocation drive consistent demand</p></div></div>
  <div class="inv-item"><svg class="icon" width="38" height="38" viewBox="0 0 38 38"><circle cx="19" cy="19" r="16"/><ellipse cx="19" cy="19" rx="7" ry="16"/><path d="M3 19h32M6 11h26M6 27h26"/></svg><div><h4>Global access</h4><p>Open to investors<br>worldwide</p></div></div>
  <div class="inv-item"><svg class="icon" width="38" height="36" viewBox="0 0 38 36"><path d="M4 12L19 4l15 8zM6 14h26M9 15v14M15 15v14M23 15v14M29 15v14M4 32h30"/></svg><div><h4>Tax advantages</h4><p>Favorable tax regime<br>for property investors</p></div></div>
  <div class="inv-item"><svg class="icon" width="36" height="38" viewBox="0 0 36 38"><path d="M18 3l13 5v10c0 9-6 14-13 17C11 32 5 27 5 18V8z"/><path d="M18 28V14M18 21c-4 0-6-2-6-6 4 0 6 2 6 6zM18 19c4 0 6-2 6-6-4 0-6 2-6 6z"/></svg><div><h4>Golden Visa program</h4><p>Residence in Europe<br>for you and your family</p></div></div>
</div>

<div class="news-line abs"></div>
<section class="news-copy abs">
  <p class="eyebrow">Golden Visa news</p>
  <h2 class="h2">Stay informed.<br>Make confident<br>decisions.</h2>
</section>
<article class="news-card abs" style="left:345px">
  <div class="news-media" role="img" aria-label="National flag waving against a blue sky" style="background:linear-gradient(160deg,#4d6a93 0%,#8ea3c0 50%,#cfd8e2 100%)"></div>
  <div class="news-body"><p class="news-date">MAY 15, 2024</p><h3 class="news-title">Greece Golden Visa<br>program update 2024</h3><p class="news-more">READ MORE <span>→</span></p></div>
</article>
<article class="news-card abs" style="left:554px">
  <div class="news-media" role="img" aria-label="Greek coastal town by calm sea at dusk" style="background:linear-gradient(180deg,#c8b89e 0%,#8f9aa0 55%,#6f7d82 100%)"></div>
  <div class="news-body"><p class="news-date">APRIL 28, 2024</p><h3 class="news-title">Top locations for real estate investment in Greece</h3><p class="news-more">READ MORE <span>→</span></p></div>
</article>
<article class="news-card abs" style="left:764px">
  <div class="news-media" role="img" aria-label="Ancient hilltop temple above the city at sunset" style="background:linear-gradient(180deg,#d8b88f 0%,#b08a63 55%,#6f5a45 100%)"></div>
  <div class="news-body"><p class="news-date">APRIL 10, 2024</p><h3 class="news-title">Why Greece remains attractive for investors</h3><p class="news-more">READ MORE <span>→</span></p></div>
</article>
<div class="news-card view-all abs" style="left:971px;width:144px">
  <svg class="icon" width="36" height="34" viewBox="0 0 36 34"><path d="M7 4h24v26H7zM7 10H3v18a2 2 0 0 0 4 0M11 9h16M11 14h7v7h-7zM21 14h6M21 18h6M11 25h16"/></svg>
  <span>SEE ALL<br>NEWS</span>
</div>

<footer class="site-footer abs"></footer>
<div class="f-brand abs"><div class="brand"><span class="brand-mark"></span>VELTAROON</div></div>
<p class="f-about abs on-dark">Boutique real estate investments in Greece with a focus on quality, trust and long-term partnerships.</p>
<div class="socials abs" aria-label="Social links"><span></span><span></span><span></span></div>
<div class="f-col abs on-dark" style="left:346px"><h5>NAVIGATION</h5>Golden Visa<br>Projects<br>Investors<br>Partners<br>About Us<br>Contact</div>
<div class="f-col abs on-dark" style="left:524px"><h5>CONTACT</h5>Lykavittou str. 18,<br>Athens 106 72, Greece
  <div class="f-contact" style="margin-top:4px"><svg width="10" height="10" viewBox="0 0 10 10"><path d="M2 1l2 2-1 1.5c.7 1.3 1.3 1.9 2.5 2.5L7 6l2 2-1 1.5C4.5 9 1 5.5.5 2z" fill="none" stroke="#c2b27f" stroke-width=".9"/></svg>+30 210 555 0186</div>
  <div class="f-contact" style="margin-top:4px"><svg width="11" height="9" viewBox="0 0 11 9"><rect x=".5" y=".5" width="10" height="8" fill="none" stroke="#c2b27f"/><path d="M.5 .5l5 4 5-4" fill="none" stroke="#c2b27f"/></svg>info@veltaroon.gr</div>
</div>
<div class="f-col abs on-dark" style="left:732px"><h5>LEGAL</h5>Privacy Policy<br>Cookies Policy<br>Terms &amp; Conditions<br>Disclaimer<br>GDPR Compliance</div>
<div class="newsletter abs on-dark">
  <h5>STAY UPDATED</h5>
  <p>Subscribe to our newsletter<br>for the latest news and offers.</p>
  <div class="nl-form"><span class="nl-input">Your email</span><span class="nl-submit"><svg width="12" height="10" viewBox="0 0 12 10"><path d="M1 5h10M7 1l4 4-4 4" fill="none" stroke="#27321f" stroke-width="1.3"/></svg></span></div>
</div>
<div class="f-bottom abs on-dark"><span>© 2024 Veltaroon Development IKE. All rights reserved.</span><span>◎ EN ⌄</span></div>

</body>
</html>
```